Bref créative
Business Stationery
Quorn Vantage
Professional
Belinda Hawthorpe
Managing Director
Arlen - Corvith - Benmere
bel@velmoragroup.com
www.velmoragroup.com
Quorn Logo
logo vector file

```html
<!DOCTYPE html>
<html lang="en">
<head>
<meta charset="utf-8">
<title>Velmora Group – Business Card</title>
<link rel="stylesheet" href="https://fonts.googleapis.com/css2?family=Open+Sans:wght@400;600;700&display=swap">
<style>
  :root {
    --page-bg: #e9e7e3;
    --card-bg: #ffffff;
    --brand-green: #3f9a2c;
    --text-dark: #3b3b3b;
    --icon-fg: #ffffff;
  }
  * { box-sizing: border-box; margin: 0; padding: 0; }
  html, body {
    width: 1200px; height: 914px; overflow: hidden;
    background: var(--page-bg);
    font-family: "Open Sans", Arial, sans-serif;
  }
  .canvas {
    width: 1200px; height: 914px;
    display: flex; align-items: center; justify-content: center;
  }
  .business-card {
    width: 900px; height: 514px;
    background: var(--card-bg);
    box-shadow: 0 6px 24px rgba(0,0,0,0.12);
    display: flex; flex-direction: column; align-items: center;
    padding-top: 130px;
  }
  .brand { display: flex; align-items: center; gap: 16px; }
  .brand-dot {
    width: 46px; height: 46px; border-radius: 50%;
    background: var(--brand-green);
  }
  .brand-name {
    font-size: 52px; font-weight: 700; color: var(--brand-green);
    letter-spacing: -1px; white-space: nowrap;
  }
  .holder {
    margin-top: 62px;
    font-size: 22px; color: var(--text-dark); white-space: nowrap;
  }
  .holder-name { color: var(--brand-green); font-weight: 600; }
  .holder-sep { margin: 0 10px; font-weight: 700; }
  .contact-row {
    display: flex; align-items: center; gap: 22px;
    font-size: 15px; color: var(--text-dark);
    margin-top: 12px; white-space: nowrap;
  }
  .holder + .contact-row { margin-top: 20px; }
  .contact-item { display: flex; align-items: center; gap: 7px; }
  .contact-icon { width: 16px; height: 16px; flex: none; }
</style>
</head>
<body>
<main class="canvas">
  <article class="business-card">
    <div class="brand">
      <span class="brand-dot"></span>
      <span class="brand-name">Velmora Group</span>
    </div>

    <p class="holder">
      <span class="holder-name">Belinda Hawthorpe</span><span class="holder-sep">|</span><span class="holder-role">Managing Director</span>
    </p>

    <div class="contact-row">
      <span class="contact-item">
        <svg class="contact-icon" viewBox="0 0 16 16" aria-hidden="true">
          <circle cx="8" cy="8" r="8" fill="var(--brand-green)"/>
          <path d="M4 8.2 8 4.5l4 3.7V12H9.5V9.5h-3V12H4z" fill="var(--icon-fg)"/>
        </svg>
        Arlen - Corvith - Benmere
      </span>
      <span class="contact-item">
        <svg class="contact-icon" viewBox="0 0 16 16" aria-hidden="true">
          <circle cx="8" cy="8" r="8" fill="var(--brand-green)"/>
          <path d="M5.2 4h1.6l.8 2-1 .8a5 5 0 0 0 2.6 2.6l.8-1 2 .8v1.6c0 .5-.5 1-1 1A7 7 0 0 1 4.2 5c0-.5.5-1 1-1z" fill="var(--icon-fg)"/>
        </svg>
        00353 55 0142 118
      </span>
    </div>

    <div class="contact-row">
      <span class="contact-item">
        <svg class="contact-icon" viewBox="0 0 16 16" aria-hidden="true">
          <circle cx="8" cy="8" r="8" fill="var(--brand-green)"/>
          <rect x="4" y="5" width="8" height="6" rx="0.8" fill="var(--icon-fg)"/>
          <path d="M4.3 5.4 8 8.3l3.7-2.9" fill="none" stroke="var(--brand-green)" stroke-width="0.9"/>
        </svg>
        bel@velmoragroup.com
      </span>
      <span class="contact-item">
        <svg class="contact-icon" viewBox="0 0 16 16" aria-hidden="true">
          <circle cx="8" cy="8" r="8" fill="var(--brand-green)"/>
          <circle cx="8" cy="8" r="4" fill="none" stroke="var(--icon-fg)" stroke-width="1"/>
          <path d="M4 8h8M8 4c-2 2.4-2 5.6 0 8M8 4c2 2.4 2 5.6 0 8" fill="none" stroke="var(--icon-fg)" stroke-width="0.8"/>
        </svg>
        www.velmoragroup.com
      </span>
      <span class="contact-item">
        <svg class="contact-icon" viewBox="0 0 16 16" aria-hidden="true">
          <circle cx="8" cy="8" r="8" fill="var(--brand-green)"/>
          <path d="M5.2 4h1.6l.8 2-1 .8a5 5 0 0 0 2.6 2.6l.8-1 2 .8v1.6c0 .5-.5 1-1 1A7 7 0 0 1 4.2 5c0-.5.5-1 1-1z" fill="var(--icon-fg)"/>
        </svg>
        00234 700 5550 129
      </span>
    </div>
  </article>
</main>
</body>
</html>
```